Accountancy firm needs clean and simple website and optional logo

We need a logo and basic wordpress website design for a Sydney based accountancy firm.
We need a clean and simple logo and website, based on the accounting/finance/tax industry. Simple, credible and official colors.
The logo is expected to be so simple that we have combined into the one job.
If you submit a logo design and we choose it along with someone else's website design you will be paid a bonus of $60. The website design will still win the competition as per normal.
Current website is old and terrible but gives you an idea of the sitemap (super simple) and what they do: www.brookfiscal.com.au
We want original different to normal template looking designs.
We like videos, and like http://www.whitfords.com.au/
Feel free to go to vidhaven and use some videos from there.
We are based in Sydney Australia and in the field of taxation and accounting
We want a clean, formal, credible site, limited pages.
The project is guaranteed, so go for it.
Brook & Associates
1 page

```html
<!DOCTYPE html>
<html lang="en">
<head>
<meta charset="utf-8">
<title>Brook &amp; Associates — Tax Accountants</title>
<link href="https://fonts.googleapis.com/css2?family=Open+Sans:wght@300;400;600;700&display=swap" rel="stylesheet">
<style>
:root{
  --blue:#1a8fe0;
  --blue-dark:#0f6fb8;
  --ink:#333a40;
  --muted:#7b848c;
  --light:#f3f5f7;
  --footer:#2b2f33;
  --white:#ffffff;
}
*{margin:0;padding:0;box-sizing:border-box}
html,body{width:861px;height:1200px;overflow:hidden}
body{font-family:"Open Sans",Arial,sans-serif;color:var(--ink);background:var(--white);position:relative}
.abs{position:absolute}

/* header */
.site-header{left:0;top:0;width:861px;height:58px;background:var(--white)}
.brand{left:30px;top:12px;display:flex;align-items:center;gap:8px}
.brand-square{width:32px;height:32px;background:var(--blue)}
.brand-name{font-size:12px;font-weight:700;color:var(--ink);letter-spacing:.5px;line-height:1.2}
.brand-name small{display:block;font-size:8px;font-weight:400;color:var(--muted);letter-spacing:.3px}
.main-nav{left:300px;top:0;display:flex;height:42px}
.main-nav a{font-size:8px;font-weight:600;color:var(--ink);text-decoration:none;padding:0 14px;line-height:42px;letter-spacing:.5px}
.main-nav a.active{background:var(--blue);color:var(--white)}
.phone{left:700px;top:14px;display:flex;align-items:center;gap:7px;font-size:13px;font-weight:600;color:var(--blue-dark)}

/* hero */
.hero{left:0;top:58px;width:861px;height:375px;background:linear-gradient(120deg,#c9c2b6 0%,#e9e6e0 45%,#9aa0a6 80%,#5b6066 100%)}
.hero-quote{left:62px;top:212px;width:480px;height:38px;background:var(--blue);color:var(--white);font-size:13px;font-weight:700;letter-spacing:.5px;display:flex;align-items:center;justify-content:center}
.hero-caption{left:230px;top:300px;width:320px;height:60px;background:rgba(255,255,255,.82);font-size:11px;letter-spacing:.4px;color:var(--ink);padding:12px 18px;line-height:1.5;text-align:center}
.hero-arrow{top:270px;width:16px;height:30px}

/* services */
.services{left:0;top:433px;width:861px;height:385px;background:var(--light)}
.services-card{left:0;top:445px;width:290px;height:160px;background:var(--white);padding:22px 30px}
.services-card h2{font-size:20px;font-weight:600;color:var(--blue);margin-bottom:12px}
.services-card li{list-style:none;font-size:8px;letter-spacing:.5px;color:var(--muted);margin-bottom:7px;padding-left:10px;position:relative}
.services-card li::before{content:"";position:absolute;left:0;top:3px;width:4px;height:4px;background:var(--blue)}
.tile{position:absolute}
.services-text{left:575px;top:608px;width:200px;height:140px;background:var(--white);padding:16px;font-size:8px;line-height:1.6;color:var(--muted)}
.btn{display:inline-block;margin-top:10px;border:1px solid var(--blue);color:var(--blue);font-size:7px;font-weight:600;padding:4px 8px;letter-spacing:.4px}

/* about */
.about-band{left:287px;top:835px;width:574px;height:215px;background:var(--blue);color:var(--white);padding:30px 40px 0 98px}
.about-band h2{font-size:20px;font-weight:600;margin-bottom:14px;letter-spacing:.5px}
.about-band p{font-size:8.5px;line-height:1.7;margin-bottom:10px;max-width:380px}
.about-band .btn{border-color:var(--white);color:var(--white);margin-top:4px}
.about-photo{left:72px;top:792px;width:305px;height:242px;background:linear-gradient(135deg,#d8dde2 0%,#b5bec6 50%,#7e8a95 100%)}

/* footer */
.footer-accent{left:0;top:1113px;width:180px;height:7px;background:var(--blue)}
.site-footer{left:0;top:1120px;width:861px;height:80px;background:var(--footer);display:flex;align-items:center;justify-content:space-between;padding:0 30px}
.site-footer p{font-size:8px;color:#aab1b7;letter-spacing:.5px}
.site-footer p span{color:var(--blue)}
.social{display:flex;gap:6px;align-items:center}
.social i{width:16px;height:16px;border-radius:50%;border:1px solid #6d747a;display:block}
.social b{font-size:8px;color:#aab1b7;font-weight:600;margin-left:8px}
</style>
</head>
<body>

<header class="site-header abs">
  <div class="brand abs">
    <span class="brand-square"></span>
    <span class="brand-name">BROOK &amp; ASSOCIATES<small>tax accountants</small></span>
  </div>
  <nav class="main-nav abs">
    <a class="active" href="#">HOME</a>
    <a href="#">ABOUT US</a>
    <a href="#">SERVICES</a>
    <a href="#">NEWS</a>
    <a href="#">CONTACT</a>
  </nav>
  <div class="phone abs">
    <svg width="14" height="14" viewBox="0 0 24 24"><path fill="#0f6fb8" d="M6.6 10.8a15.1 15.1 0 0 0 6.6 6.6l2.2-2.2c.3-.3.7-.4 1-.2 1.1.4 2.3.6 3.6.6.6 0 1 .4 1 1V20c0 .6-.4 1-1 1A17 17 0 0 1 3 4c0-.6.4-1 1-1h3.5c.6 0 1 .4 1 1 0 1.3.2 2.5.6 3.6.1.3 0 .7-.2 1z"/></svg>
    02 9000 4127
  </div>
</header>

<section class="hero abs" role="img" aria-label="Photo of a desk with laptop, documents and coffee cup"></section>
<svg class="hero-arrow abs" style="left:6px" viewBox="0 0 16 30"><polyline points="12,4 4,15 12,26" fill="none" stroke="#fff" stroke-width="2"/></svg>
<svg class="hero-arrow abs" style="left:839px" viewBox="0 0 16 30"><polyline points="4,4 12,15 4,26" fill="none" stroke="#fff" stroke-width="2"/></svg>
<div class="hero-quote abs">“ TAKE THE WORRY OUT OF TAX AND BUSINESS ”</div>
<div class="hero-caption abs">LOREM IPSUM DOLOR SIT AMET, CONSECTETUR ADIPISCING ELIT AENEAN COMMODO</div>

<section class="services abs">
</section>
<div class="services-card abs">
  <h2>SERVICES</h2>
  <ul>
    <li>ACCOUNTING</li>
    <li>FINANCE</li>
    <li>TAX</li>
  </ul>
</div>
<div class="tile" style="left:290px;top:455px;width:140px;height:150px;background:linear-gradient(135deg,#e4e7ea,#b9c1c8)" role="img" aria-label="Photo of hands with calculator and papers"></div>
<div class="tile" style="left:430px;top:455px;width:140px;height:150px;background:linear-gradient(135deg,#3d8fd8,#1b5fa8)" role="img" aria-label="Photo of blue calculator keys"></div>
<div class="tile" style="left:570px;top:495px;width:150px;height:110px;background:linear-gradient(135deg,#7fb4e4,#2e75c0)" role="img" aria-label="Photo of financial charts on screen"></div>
<div class="tile" style="left:720px;top:495px;width:110px;height:110px;background:linear-gradient(135deg,#eef0f2,#c3c9cf)" role="img" aria-label="Photo of a person writing at a desk"></div>
<div class="tile" style="left:80px;top:605px;width:165px;height:140px;background:linear-gradient(135deg,#dfe3e6,#a8b1b9)" role="img" aria-label="Photo of a calculator on documents"></div>
<div class="tile" style="left:245px;top:605px;width:155px;height:140px;background:linear-gradient(135deg,#5a9bd8,#225f9e)" role="img" aria-label="Photo of financial papers and pen"></div>
<div class="tile" style="left:400px;top:605px;width:170px;height:140px;background:linear-gradient(135deg,#e9ebed,#9ea7af)" role="img" aria-label="Photo of a magnifying glass over tax forms"></div>
<div class="services-text abs">
  We prepare clear accounts and tax returns for individuals and small businesses across Sydney, with advice you can rely on.
  <br><span class="btn">READ MORE</span>
</div>

<section class="about-band abs">
  <h2>ABOUT BROOK TAX</h2>
  <p>We collect and review your records each year so your returns are lodged on time and your business stays in good standing with the regulator.</p>
  <p>We never share your information with other companies, and any details given to us are treated in confidence. You can rely on us whenever you need help.</p>
  <span class="btn">READ MORE</span>
</section>
<div class="about-photo abs" role="img" aria-label="Photo of business advisers meeting at a table"></div>

<div class="footer-accent abs"></div>
<footer class="site-footer abs">
  <p>© COPYRIGHT 2015 BY <span>BROOK TAX</span> . ALL RIGHTS RESERVED</p>
  <div class="social"><i></i><i></i><i></i><i></i><i></i><b>ENG</b></div>
</footer>

</body>
</html>
```